IT Company Business Card Design w/Stationary Design

We have a great logo we like! We are looking to redesign our business cards and all company logo'd merchandise/materials.

We are an IT Company located near the Bay Area (San Francisco, CA). We specialize in Managed Services and offer complete IT Computer and Network Support to Businesses of all sizes. We thrive on making a lasting impression. We have been doing IT for 15yrs+ but are young at heart. We like to stand out and be different. We want to be unique and have a recognizable brand. We need our logo to represent who we are. We are young, professional, creative and outstanding. We don't want to blend in, we want to stand out. Our business card needs to stand out and grab attention. Something Bold, yet simple and clean. (I will provide ideas of what we like to give a taste of what we are looking for).

The design can include any kind of texture/artistic design or sizing EXCEPT please "no square card designs" as they don't seem to fit in wallets very well. We dont mind curved edges, rounded corners, vertical layouts or horizontal layouts, embossing, letter press or raised surfaces. Again, we dont want to look average or plain or boring. :) Be creative - yet practical! We have ordered from ZEPL designs before and been very happy. Their card sizes tend to be a little different, so beware. Hope this helps!

Target Market(s)

Businesses - Small to Medium, Corporations, Publicly Traded Companies

Industry/Entity Type

Business

Contact Information for Business Card

Harbor Circuit IT
7180 Dorrance Avenue
Suite K
Modesto, CA 95419

Office 209.555.0137
Direct 209.555.0162
Cell 209.555.0188

Gary Stroud
Founder, CEO
www.hcxit.example
gstroud@hcxit.example

Locations Serviced: Modesto, Stockton, Pleasanton, Fresno (incorporate this on the card ONLY if there's a good place to do so).

What we specialize in: Computer, Network, Voice, Data. (IT Services)

Our Logo Colors: Black and Blue (#006699). Open to using grey or orange as well - but not required. Don't want too busy....

Logo Font: "Voralyn" (Will attach logo font). We want type style to be clean. You can show different font types including our logo font - and we are open to other font ideas.

The logo can be separated. You can use elements together or apart. Surprise us! :) We "REALLY" want the "hc" to be our identifier/our brand people recognize.

Font styles to use
Sans Serif

Colors
0355a3
3176b5
f37122
f78f20
faa54b
474747
aaaaaa
757575
000000

Requirements
Must have
• Bold, Big, Colorful, Modern/yet Fun, Clean Design, Stand Out Presence, Texture would be welcomed - but not necessary, Card design shape can include cut corners or rounded or square edges. Be creative. (HOWEVER, we don't want a square design because we have found it doesn't fit in wallets that easily).
• We do like using ZEPL printing company (Which they have particular sizing on their card templates - beware), but are open to other design templates/printing companies as well. We just want to make sure its easy to find a print company to do our work. Too unique could be costly and hard to get cards printed.
• Colors to use: Our logo Blue (#006699), with either whites, grays, black, shades of our blue, and maybe a pinch of orange if needed. Primarily, blue, white, gray or black.
Nice to have
• Texture would be cool or little different edging or shape - but nothing too costly to print. I have seen cards with 3 sharp edges and one round edge. Something like that would be cool as an option. Or a vertical card.
• I love a faded watermark look. It would be nice to see some shading of our circle logo on a few designs. The circle with "hc" in it OR.... taking just the "hc" and using it alone.
Should not have
• No square card designs. Nothing too expensive or elaborate to print. No busy fonts. Do not like Times New Roman type fonts (too old looking). Not a lot of orange (if you even choose to use some orange).

```html
<!DOCTYPE html>
<html lang="en">
<head>
<meta charset="utf-8">
<title>Harbor Circuit IT — Business Card</title>
<link rel="stylesheet" href="https://fonts.googleapis.com/css2?family=Didact+Gothic&display=swap">
<style>
  :root {
    --brand-blue: #1a8fc8;
    --brand-blue-deep: #0b6aa6;
    --brand-blue-light: #22a2db;
    --ink: #3a3a3a;
    --muted: #9a9a9a;
    --rule: #d4d4d4;
    --paper: #f7f7f7;
    --backdrop: #a3a3a3;
    --white: #ffffff;
  }
  * { box-sizing: border-box; margin: 0; padding: 0; }
  html, body { width: 1200px; height: 900px; overflow: hidden; }
  body {
    background: var(--backdrop);
    font-family: "Didact Gothic", "Century Gothic", sans-serif;
    position: relative;
  }
  .card {
    position: absolute;
    left: 250px;
    width: 700px;
    height: 400px;
    border-radius: 24px;
    overflow: hidden;
    box-shadow: 0 6px 18px rgba(0,0,0,0.25);
  }
  .card--front { top: 40px; background: var(--paper); }
  .card--back {
    top: 460px;
    background: linear-gradient(135deg, var(--brand-blue-light) 0%, var(--brand-blue) 45%, var(--brand-blue-deep) 100%);
    display: flex; align-items: center; justify-content: center;
  }

  .brand {
    position: absolute; left: 0; top: 0; width: 320px; height: 400px;
    display: flex; flex-direction: column; align-items: center; justify-content: center; gap: 26px;
  }
  .brand__dot { width: 110px; height: 110px; border-radius: 50%; background: var(--brand-blue); }
  .brand__name { color: var(--brand-blue); font-size: 34px; letter-spacing: 1px; }

  .divider { position: absolute; left: 330px; top: 40px; width: 1px; height: 320px; background: var(--rule); }

  .contact { position: absolute; left: 360px; top: 44px; width: 320px; }
  .contact__name { color: var(--brand-blue); font-size: 27px; letter-spacing: 1.5px; }
  .contact__title { color: var(--muted); font-size: 20px; letter-spacing: 1.5px; margin-top: 4px; }
  .contact__address { color: var(--ink); font-size: 17px; line-height: 23px; margin-top: 16px; }
  .contact__list { list-style: none; margin-top: 16px; }
  .contact__item {
    display: flex; align-items: center; gap: 12px;
    color: var(--ink); font-size: 18px; line-height: 27px; letter-spacing: 0.5px;
  }
  .contact__icon { width: 16px; height: 16px; fill: var(--brand-blue); flex: none; }

  .back__name { color: var(--white); font-size: 64px; letter-spacing: 2px; }
</style>
</head>
<body>
  <section class="card card--front" aria-label="Business card front">
    <div class="brand">
      <div class="brand__dot"></div>
      <div class="brand__name">Harbor Circuit</div>
    </div>
    <div class="divider"></div>
    <div class="contact">
      <div class="contact__name">Gary Stroud</div>
      <div class="contact__title">Founder, CEO</div>
      <div class="contact__address">Harbor Circuit IT<br>7180 Dorrance Avenue<br>Suite K Modesto, CA 95419</div>
      <ul class="contact__list">
        <li class="contact__item">
          <svg class="contact__icon" viewBox="0 0 16 16"><rect x="1" y="6" width="14" height="9" rx="2"/><path d="M1 5c2-3 12-3 14 0v1H1z"/></svg>209.555.0137
        </li>
        <li class="contact__item">
          <svg class="contact__icon" viewBox="0 0 16 16"><path d="M4 1l3 3-2 2c1 2 3 4 5 5l2-2 3 3-2 3C7 15 1 9 1 3z"/></svg>209.555.0162
        </li>
        <li class="contact__item">
          <svg class="contact__icon" viewBox="0 0 16 16"><path d="M4 0h8a1 1 0 0 1 1 1v14a1 1 0 0 1-1 1H4a1 1 0 0 1-1-1V1a1 1 0 0 1 1-1zm1 2v10h6V2z"/></svg>209.555.0188
        </li>
        <li class="contact__item">
          <svg class="contact__icon" viewBox="0 0 16 16"><path d="M0 3h16v10H0zM1 4l7 5 7-5v-.2H1z" fill-rule="evenodd"/></svg>gstroud@hcxit.example
        </li>
        <li class="contact__item">
          <svg class="contact__icon" viewBox="0 0 16 16"><circle cx="8" cy="8" r="7" fill="none" stroke="#1a8fc8" stroke-width="1.4"/><ellipse cx="8" cy="8" rx="3" ry="7" fill="none" stroke="#1a8fc8" stroke-width="1.2"/><path d="M1 8h14" stroke="#1a8fc8" stroke-width="1.2"/></svg>www.hcxit.example
        </li>
      </ul>
    </div>
  </section>

  <section class="card card--back" aria-label="Business card back">
    <div class="back__name">Harbor Circuit</div>
  </section>
</body>
</html>
```